Business Card for a Life Coaching Company

BRAVOPEAK is a Life Coaching company that was initiated to support people who want to transform thier life or ana aspect of it.
our slogan is : "Dream. Believe. Succeed"
our logo is uploaded.
The name of the company implies that leadership, strength and wisdom required to change your life.
We want an attractive business card that would give an impression of reliability, support and change. so we really want it unique. Here are some examples of unique cards:

http://www.cardcraftvault.example/2009/05/100-really-creative-business-cards/

BravoPeak is a life coaching organization focusing on individual transformation through the application of relevant and timeless principles of success.  BravoPeak believes that real, sustainable life transformations are brought about by tuning into the timeless wisdom we each carry in our hearts while boldy acting in the direction of our dreams.

Contacts on the card:
Address: 7 Tarek Nour El Dine Heliopolis Cairo Egypt
Tel: +202 24 71 38 52
Fax: +202 24 71 38 17
Mobile: +2 012 684 2097 (Dalia Soliman)
+2 0199915815 (Tariq Bhatti)

By the way, our temporary website is http://www.bravopeak.example

We have attached an .eps file with various configurations of our logo.

```html
<!DOCTYPE html>
<html lang="en">
<head>
<meta charset="utf-8">
<title>BravoPeak Business Card</title>
<link rel="stylesheet" href="https://fonts.googleapis.com/css2?family=Quicksand:wght@400;500&display=swap">
<style>
  :root {
    --orange: #e05a22;
    --grey-dark: #8c8e90;
    --grey-light: #a09e9c;
    --glow-core: #fbd23a;
    --glow-mid: #f29a1c;
    --white: #ffffff;
    --page: #ffffff;
  }
  * { margin: 0; padding: 0; box-sizing: border-box; }
  html, body {
    width: 1200px;
    height: 354px;
    overflow: hidden;
    background: var(--page);
    font-family: "Quicksand", sans-serif;
    color: var(--white);
  }
  .canvas { position: relative; width: 1200px; height: 354px; }

  .card { position: absolute; top: 22px; width: 558px; height: 309px; background: var(--white); overflow: hidden; }
  .card--front { left: 20px; }
  .card--back { left: 621px; width: 559px; }

  .panel { position: absolute; top: 0; height: 100%; }
  .panel--orange { background: var(--orange); }
  .panel--grey { background: linear-gradient(90deg, var(--grey-dark), var(--grey-light)); }

  .card--front .panel--orange { left: 0; width: 224px; }
  .card--front .panel--grey { left: 226px; width: 332px; }

  .emblem-glow {
    position: absolute;
    left: 80px; top: 40px;
    width: 240px; height: 240px;
    border-radius: 50%;
    background: radial-gradient(circle, var(--glow-core) 0%, var(--glow-mid) 35%, rgba(224,90,34,0) 70%);
  }

  .brand-name {
    position: absolute;
    left: 238px;
    top: 78px;
    font-weight: 400;
    font-size: 64px;
    line-height: 64px;
    letter-spacing: 1px;
    color: var(--white);
  }

  .slogan-band { position: absolute; top: 221px; height: 27px; left: 0; width: 100%; }
  .slogan-band__left { position: absolute; left: 0; width: 224px; height: 100%; background: var(--grey-dark); }
  .slogan-band__right { position: absolute; left: 226px; width: 332px; height: 100%; background: var(--orange); }
  .slogan { position: absolute; top: 4px; font-size: 15px; letter-spacing: 0.5px; white-space: nowrap; }
  .slogan--first { right: 10px; }
  .slogan--rest { left: 22px; }

  .card--back .panel--grey { left: 0; width: 224px; }
  .card--back .panel--orange { left: 226px; width: 333px; }

  .contact-person { position: absolute; left: 41px; top: 144px; font-size: 19px; font-weight: 400; white-space: nowrap; }
  .designation { position: absolute; right: 30px; top: 170px; font-size: 12px; white-space: nowrap; }

  .contact-list { position: absolute; left: 58px; top: 0; width: 260px; font-size: 13.5px; }
  .contact-row { position: absolute; left: 0; white-space: nowrap; }
  .contact-row .label { display: inline-block; width: 56px; }
  .contact-row .sep { display: inline-block; width: 15px; }
</style>
</head>
<body>
<div class="canvas">
  <section class="card card--front">
    <div class="panel panel--orange">
      <div class="emblem-glow" role="img" aria-label="Warm sunburst glow behind the brand name"></div>
    </div>
    <div class="panel panel--grey"></div>
    <div class="brand-name">BRAVO<br>PEAK</div>
    <div class="slogan-band">
      <div class="slogan-band__left"><span class="slogan slogan--first">"Dream</span></div>
      <div class="slogan-band__right"><span class="slogan slogan--rest">Believe &nbsp;|&nbsp;&nbsp; Succeed"</span></div>
    </div>
  </section>

  <section class="card card--back">
    <div class="panel panel--grey">
      <div class="contact-person">Contact Person</div>
      <div class="designation">Designation</div>
    </div>
    <div class="panel panel--orange">
      <div class="contact-list">
        <div class="contact-row" style="top:87px"><span class="label">office</span><span class="sep">:</span></div>
        <div class="contact-row" style="top:120px"><span class="label">tel</span><span class="sep">:</span>+00-000-000-00</div>
        <div class="contact-row" style="top:137px"><span class="label">fax</span><span class="sep">:</span>+00-000-000-00</div>
        <div class="contact-row" style="top:172px"><span class="label">e-mail</span><span class="sep">:</span>info@bravopeak.com</div>
        <div class="contact-row" style="top:207px"><span class="label">visit us</span><span class="sep">:</span>www.bravopeak.com</div>
      </div>
    </div>
  </section>
</div>
</body>
</html>
```